Lantern Airfields Homepage Design Update

here's the current site - http://lanternairfields.example/

client is not happy with overall look.

keeping the same info - intro text, headlines, featured media excepts and general navigation options - can you come up with a nicer, slicker look for this homepage?

UPDATE: since it was asked by designer.. the general layout doesnt have to be the same. its not required to have a big image, with text below that and then smaller images/text below that. as long as we have the same content on the page, it can organized and designed in any way,

client like big images, so one way or the other, keep that... but feel free to reorganize content, explore different ways of framing it, and/or anything else. make this homepage pop!

for the designer that wins this, we'll start an additional project to update the interior.

let me know if any questions..

thanks!

marcus

Target Market(s)

aviation industry professionals, local governments, general public

Number of Pages Required

1 page

Font styles to use
Sans Serif

Requirements
Must have
• big image somewhere. same content as on current site, just designed differently.

```html
<!DOCTYPE html>
<html lang="en">
<head>
<meta charset="utf-8">
<title>Lantern Airfields</title>
<link rel="stylesheet" href="https://fonts.googleapis.com/css2?family=Open+Sans:wght@400;600;700;800&display=swap">
<style>
  :root {
    --brand-blue: #1f3f9e;
    --accent-green: #7cc223;
    --ink: #1b1b1b;
    --nav-grey: #9a9a9a;
    --logo-grey: #5b6b86;
    --muted: #8c8c8c;
    --card-bg: #ffffff;
    --page-bg: #ffffff;
    --sky-deep: #6fa3dc;
    --sky-mid: #a9cbee;
    --cloud: #f3f6fa;
  }
  * { box-sizing: border-box; margin: 0; padding: 0; }
  html, body { width: 1200px; height: 900px; overflow: hidden; background: var(--page-bg); }
  body { font-family: "Open Sans", Arial, sans-serif; color: var(--ink); position: relative; }

  .site-header { position: absolute; top: 0; left: 0; width: 1200px; height: 64px; background: #fff; }
  .logo { position: absolute; left: 130px; top: 22px; display: flex; align-items: center; gap: 8px; font-size: 17px; font-weight: 400; color: var(--logo-grey); letter-spacing: 0.5px; }
  .logo-dot { width: 10px; height: 10px; border-radius: 50%; border: 1.5px solid var(--logo-grey); }
  .main-nav { position: absolute; left: 520px; top: 0; height: 64px; display: flex; }
  .main-nav a { display: flex; align-items: center; padding: 0 15px; font-size: 11px; color: var(--nav-grey); text-decoration: none; letter-spacing: 0.3px; }
  .main-nav a.is-active { background: var(--brand-blue); color: #fff; font-weight: 600; }

  .hero { position: absolute; top: 64px; left: 0; width: 1200px; height: 320px; overflow: hidden;
    background: linear-gradient(180deg, var(--sky-deep) 0%, var(--sky-mid) 30%, #d3e3f3 62%, #eef3f9 84%, #ffffff 100%); }
  .hero-sheen { position: absolute; inset: 0; }

  .welcome { position: absolute; top: 402px; left: 0; width: 1200px; text-align: center; font-size: 22px; font-weight: 800; letter-spacing: 2px; }
  .welcome .highlight { color: var(--accent-green); }
  .welcome-chevron { position: absolute; top: 436px; left: 592px; }

  .about { position: absolute; top: 462px; left: 0; width: 1200px; height: 190px; display: flex; }
  .about-photo { width: 560px; height: 100%;
    background: linear-gradient(180deg, #1e1f22 0%, #3c3e42 22%, #9ea3a8 48%, #d9dcde 62%, #6e7276 80%, #2a2c2f 100%); }
  .about-panel { flex: 1; background: var(--brand-blue); color: #fff; padding: 30px 0 0 120px; position: relative; overflow: hidden; }
  .about-panel p { position: relative; width: 420px; font-size: 11px; line-height: 1.55; letter-spacing: 0.2px; }
  .about-sheen { position: absolute; inset: 0; }
  .about-badge { position: absolute; left: 525px; top: 60px; width: 70px; height: 70px; border-radius: 50%; background: #fff; box-shadow: 0 2px 8px rgba(0,0,0,0.25); display: flex; align-items: center; justify-content: center; text-align: center; font-size: 9px; font-weight: 700; line-height: 1.3; }

  .news-grid { position: absolute; top: 668px; left: 150px; width: 900px; display: grid; grid-template-columns: 440px 440px; gap: 12px 20px; }
  .news-card { height: 106px; background: var(--card-bg); box-shadow: 0 1px 6px rgba(0,0,0,0.12); display: flex; position: relative; }
  .news-card.is-reversed { flex-direction: row-reverse; }
  .news-media { width: 220px; height: 100%; }
  .media-gear { background: linear-gradient(135deg, #2b2e33 0%, #4d535b 35%, #8d96a0 60%, #c9d3dc 85%, #e3e6e4 100%); }
  .media-plane { background: linear-gradient(180deg, #6fa3dc 0%, #a9cbee 45%, #e2edf8 78%, #ffffff 100%); }
  .media-tourist { background: linear-gradient(180deg, #8fb9e4 0%, #c8dcef 45%, #b9a58a 75%, #6d5c48 100%); }
  .media-runway { background: linear-gradient(180deg, #121826 0%, #26304a 45%, #4d5a78 75%, #8c93a6 100%); }
  .news-body { flex: 1; padding: 24px 18px 0 20px; }
  .news-author { font-size: 8px; color: var(--muted); text-transform: uppercase; letter-spacing: 0.3px; }
  .news-title { font-size: 12px; font-weight: 700; color: var(--brand-blue); text-transform: uppercase; margin-top: 2px; }
  .news-excerpt { font-size: 9px; color: var(--muted); line-height: 1.5; margin-top: 8px; }
  .plus-btn { position: absolute; top: 41px; left: 208px; width: 24px; height: 24px; border-radius: 50%; background: var(--brand-blue); }
  .plus-btn svg { display: block; }
</style>
</head>
<body>
  <header class="site-header">
    <div class="logo"><span class="logo-dot"></span>Lantern Airfields</div>
    <nav class="main-nav">
      <a href="#" class="is-active">HOME</a>
      <a href="#">ABOUT US</a>
      <a href="#">AIRPORTS</a>
      <a href="#">NEWS AND MEDIA</a>
      <a href="#">CONTACT US</a>
      <a href="#">EMPLOYEES</a>
    </nav>
  </header>

  <section class="hero" role="img" aria-label="Passenger jet flying low overhead against a blue sky with white clouds">
    <svg class="hero-sheen" width="1200" height="320" viewBox="0 0 1200 320">
      <polygon points="640,0 1200,0 1200,320 860,320" fill="#ffffff" fill-opacity="0.16"/>
    </svg>
  </section>

  <h1 class="welcome">WELCOME TO <span class="highlight">LANTERN AIRFIELDS</span></h1>
  <svg class="welcome-chevron" width="16" height="10" viewBox="0 0 16 10">
    <polyline points="2,8 8,2 14,8" fill="none" stroke="#1f3f9e" stroke-width="1.5"/>
  </svg>

  <section class="about">
    <div class="about-photo" role="img" aria-label="Silhouette of a traveler standing at a large terminal window"></div>
    <div class="about-panel">
      <svg class="about-sheen" width="640" height="190" viewBox="0 0 640 190">
        <polygon points="380,0 640,0 640,190 520,190" fill="#ffffff" fill-opacity="0.1"/>
      </svg>
      <p>Lantern Airfields is focused on opportunities to invest, develop and manage both general aviation and commercial service airports in key U.S. markets. A subsidiary of Lantern Investments, a private equity firm that exclusively invests in the Aerospace &amp; Transportation sectors, Lantern has the resources available to invest and finance transactions.<br>Lantern maintains offices in New York, Dublin and Atlanta.</p>
    </div>
    <div class="about-badge">ABOUT<br>US</div>
  </section>

  <section class="news-grid">
    <article class="news-card">
      <div class="news-media media-gear" role="img" aria-label="Travel gear, camera and passport on a map"></div>
      <span class="plus-btn"><svg width="24" height="24" viewBox="0 0 24 24"><path d="M12 7v10M7 12h10" stroke="#fff" stroke-width="2"/></svg></span>
      <div class="news-body">
        <div class="news-author">By Admin</div>
        <h2 class="news-title">Lantern Travel</h2>
        <p class="news-excerpt">Quick notes on routes, terminals and fresh updates for travelers.</p>
      </div>
    </article>
    <article class="news-card is-reversed">
      <div class="news-media media-plane" role="img" aria-label="Airliner in flight above clouds"></div>
      <span class="plus-btn"><svg width="24" height="24" viewBox="0 0 24 24"><path d="M12 7v10M7 12h10" stroke="#fff" stroke-width="2"/></svg></span>
      <div class="news-body">
        <div class="news-author">By Dorian</div>
        <h2 class="news-title">New Offers</h2>
        <p class="news-excerpt">Seasonal deals on parking, lounges and services across our airports.</p>
      </div>
    </article>
    <article class="news-card">
      <div class="news-media media-tourist" role="img" aria-label="Traveler with a camera outdoors"></div>
      <span class="plus-btn"><svg width="24" height="24" viewBox="0 0 24 24"><path d="M12 7v10M7 12h10" stroke="#fff" stroke-width="2"/></svg></span>
      <div class="news-body">
        <div class="news-author">By Felix Ward</div>
        <h2 class="news-title">What We Offer ?</h2>
        <p class="news-excerpt">Investment, development and management for commercial airfields.</p>
      </div>
    </article>
    <article class="news-card is-reversed">
      <div class="news-media media-runway" role="img" aria-label="Airplane nose on a runway at dusk"></div>
      <span class="plus-btn"><svg width="24" height="24" viewBox="0 0 24 24"><path d="M12 7v10M7 12h10" stroke="#fff" stroke-width="2"/></svg></span>
      <div class="news-body">
        <div class="news-author">By Owen Pratt</div>
        <h2 class="news-title">Airplane</h2>
        <p class="news-excerpt">A closer look at the aircraft moving through our busy hubs today.</p>
      </div>
    </article>
  </section>
</body>
</html>
```